App "loading/waiting" animated GIF

We need an original "loading/waiting" animated GIF to fit our desktop app design (linked)
The app logo and the hexagon shape could be an inspiration source, "Artificial Intelligence" is the main topic of this app.
In general the user have to wait between 1s and 10s
The GIF should fit inside a 300px square (with a 2x resolution version)

Colors
33a6d7
0455a3

```html
<!DOCTYPE html>
<html lang="en">
<head>
<meta charset="UTF-8">
<title>Initializing</title>
<link rel="stylesheet" href="https://fonts.googleapis.com/css2?family=Fira+Sans:wght@600&display=swap">
<style>
  :root {
    --bg: #000000;
    --accent: #33a6d7;
    --line: #ffffff;
  }
  html, body {
    margin: 0;
    padding: 0;
    width: 1200px;
    height: 1200px;
    overflow: hidden;
    background: var(--bg);
  }
  .loader {
    position: relative;
    width: 1200px;
    height: 1200px;
  }
  .loader__art {
    position: absolute;
    inset: 0;
  }
  .hex-accent { stroke: var(--accent); }
  .hex-light { stroke: var(--line); }
  .hex-accent, .hex-light {
    fill: none;
    stroke-width: 6;
    stroke-linecap: butt;
    stroke-linejoin: miter;
  }
  .progress-track {
    fill: none;
    stroke: var(--line);
    stroke-width: 4;
  }
  .loader__status {
    position: absolute;
    left: 0;
    top: 470px;
    width: 1200px;
    margin: 0;
    text-align: center;
    font-family: "Fira Sans", sans-serif;
    font-weight: 600;
    font-size: 40px;
    line-height: 52px;
    letter-spacing: 1px;
    color: var(--accent);
  }
</style>
</head>
<body>
<main class="loader">
  <svg class="loader__art" width="1200" height="1200" viewBox="0 0 1200 1200" aria-hidden="true">
    <g class="hexagon">
      <path class="hex-light" d="M556,270 L474,318"/>
      <path class="hex-accent" d="M474,318 L376,376 L376,464"/>
      <path class="hex-light" d="M376,566 L376,632 L404,648"/>
      <path class="hex-accent" d="M404,648 L576,748"/>
      <path class="hex-light" d="M666,724 L750,676"/>
      <path class="hex-accent" d="M750,676 L824,632 L824,516"/>
      <path class="hex-light" d="M824,414 L824,376 L774,346"/>
      <path class="hex-accent" d="M774,346 L600,246"/>
    </g>
    <rect class="progress-track" x="256" y="832" width="686" height="44"/>
  </svg>
  <p class="loader__status">initializing...</p>
</main>
</body>
</html>
```